弊社のサービスが一目で伝わるデザインを希望します。コロナ禍でチラシを受け取りたくない方も大勢いらっしゃると思いますが、そんな中でも手に取っていただけるような明るい雰囲気が良いかと思います。サービスの良い点を前面にアピールしてください。両面希望ですが、ポスターにも流用希望ですので、片面でも充分伝わる内容でお願いします。弊社サービスは3パターンあり、パンフレットに挟んでお客様へお渡ししたいと思います。3パターン合計の費用となります。

```html
<!DOCTYPE html>
<html lang="ja">
<head>
<meta charset="utf-8">
<title>健康診断 Web問診サービス</title>
<link href="https://fonts.googleapis.com/css2?family=Noto+Sans+JP:wght@400;500;700;900&family=Noto+Serif+JP:wght@600;700;900&display=swap" rel="stylesheet">
<style>
:root{
  --blue:#1d5ea8;
  --blue-dark:#123f78;
  --blue-light:#e4eef8;
  --red:#d9353a;
  --orange:#ee8a1f;
  --green:#7bb22f;
  --sky:#2e8bd3;
  --gray:#8a8f96;
  --ink:#333a42;
  --paper:#ffffff;
  --sand:#fbf4ea;
}
*{box-sizing:border-box;margin:0;padding:0}
html,body{width:854px;height:1200px;overflow:hidden;background:var(--paper)}
body{font-family:"Noto Sans JP",sans-serif;color:var(--ink);position:relative}

.hero{position:absolute;left:0;top:0;width:854px;height:300px;overflow:hidden}
.hero-photo{position:absolute;inset:0;background:linear-gradient(100deg,#b9c9d6 0%,#dfe7ee 35%,#f4f7fa 60%,#ffffff 100%)}
.title-band{position:absolute;left:150px;top:8px;width:560px;height:70px;background:var(--blue);border-radius:6px;color:#fff;display:flex;align-items:center;justify-content:center;gap:8px;box-shadow:0 3px 0 var(--blue-dark)}
.title-band .small{font-size:34px;font-weight:900;letter-spacing:2px}
.title-band .big{font-family:"Noto Serif JP",serif;font-size:50px;font-weight:900}
.title-band .mid{font-size:34px;font-weight:900;letter-spacing:2px}
.worry{position:absolute;left:420px;top:90px;width:420px}
.worry h2{font-family:"Noto Serif JP",serif;font-size:20px;color:var(--blue-dark);font-weight:700;margin-bottom:8px;white-space:nowrap}
.worry p{font-size:15px;line-height:1.65;color:var(--ink);font-weight:500;white-space:nowrap}

.flow{position:absolute;left:0;top:230px;width:854px;height:200px}
.flow-user{position:absolute;left:40px;top:20px;width:130px;height:110px;border-radius:12px;background:linear-gradient(#fdf6f6,#f0e6e6)}
.flow-staff{position:absolute;right:40px;top:20px;width:130px;height:110px;border-radius:12px;background:linear-gradient(#eef4fa,#d9e6f2)}
.flow-label{position:absolute;font-size:12px;line-height:1.45;font-weight:500;background:#fff;border:1px solid #c9d6e3;padding:4px 8px;border-radius:4px}
.flow-label.left{left:30px;top:140px;width:180px}
.flow-label.right{right:30px;top:140px;width:190px}
.flow-center{position:absolute;left:307px;top:8px;width:240px;height:160px}
.flow-center .tag{position:absolute;left:62px;top:4px;font-size:14px;font-weight:700;color:var(--blue);transform:rotate(-8deg)}
.flow-center .node{position:absolute;left:78px;top:30px;width:84px;height:66px;background:var(--blue);border-radius:10px;color:#fff;font-size:11px;font-weight:700;text-align:center;display:flex;align-items:center;justify-content:center;line-height:1.3}
.flow-center .cap{position:absolute;left:60px;top:132px;width:120px;text-align:center;font-size:14px;font-weight:700;color:var(--blue-dark);background:#fff;border:2px solid var(--blue);border-radius:4px}

.section-head{position:absolute;left:0;width:854px;text-align:center;font-family:"Noto Serif JP",serif;font-weight:900;color:var(--red)}
.benefits-head{top:436px;font-size:28px}
.benefits-head .num{font-size:50px;color:var(--orange);vertical-align:-6px;margin:0 6px}
.benefits-head .rule{display:block;width:620px;height:3px;background:var(--orange);margin:2px auto 0}
.steps-head{top:812px;font-size:22px;color:var(--red)}
.steps-head::before,.steps-head::after{content:"";display:inline-block;width:150px;height:2px;background:var(--orange);vertical-align:middle;margin:0 14px}

.cards{position:absolute;left:22px;width:810px;display:grid;grid-template-columns:repeat(4,1fr);gap:10px}
.benefits{top:512px}
.steps{top:856px}
.card{background:#fff;border:1px solid #e1e4e8;border-radius:6px;box-shadow:0 2px 4px rgba(0,0,0,.08);padding:10px;height:280px;position:relative}
.steps .card{height:230px;background:var(--sand)}
.card-top{display:flex;align-items:center;gap:8px;height:58px}
.badge{flex:none;width:44px;height:48px;border-radius:4px;color:#fff;font-size:30px;font-weight:900;display:flex;align-items:center;justify-content:center}
.card-title{font-size:17px;font-weight:900;line-height:1.25;color:var(--ink)}
.kicker{font-size:11px;font-weight:700;color:var(--gray);margin:8px 0 4px}
.card p{font-size:12px;line-height:1.6}
.card .pic{position:absolute;left:10px;right:10px;bottom:10px;height:62px;border-radius:4px;background:linear-gradient(#eef3f8,#dfe8f1)}
.c-red{background:var(--red)}.c-orange{background:var(--orange)}.c-green{background:var(--green)}.c-sky{background:var(--sky)}.c-gray{background:var(--gray)}

.footer{position:absolute;left:0;top:1104px;width:854px;height:96px;background:var(--blue);color:#fff;padding:12px 28px}
.footer .company{font-size:24px;font-weight:700;letter-spacing:1px}
.footer .address{font-size:11px;margin-top:6px;opacity:.9}
.footer .note{position:absolute;right:28px;top:14px;font-size:11px;opacity:.9}
.footer .tel{position:absolute;right:28px;top:42px;font-size:26px;font-weight:700;display:flex;gap:28px;align-items:center}
.footer .tel span{font-size:14px;margin-right:4px}
</style>
</head>
<body>

<header class="hero">
  <div class="hero-photo" role="img" aria-label="マスクと医療用キャップを着用した医療従事者の写真"></div>
  <div class="title-band"><span class="small">健康診断</span><span class="big">Web</span><span class="mid">問診サービス</span></div>
  <div class="worry">
    <h2>こんなことでお困りではありませんか？</h2>
    <p>感染リスクを減らすために、待ち時間を<br>少なくしたい。時間をかけずにスマートに<br>問診をデータで管理したい・・・</p>
  </div>
</header>

<section class="flow">
  <div class="flow-user" role="img" aria-label="パソコンを使う利用者のキャラクターイラスト"></div>
  <div class="flow-staff" role="img" aria-label="マスク姿の医療従事者のイラスト"></div>
  <svg width="854" height="200" style="position:absolute;left:0;top:0">
    <path d="M180 70 H300" stroke="#ee8a1f" stroke-width="8"/><path d="M300 58 L318 70 L300 82Z" fill="#ee8a1f"/>
    <path d="M674 70 H554" stroke="#ee8a1f" stroke-width="8"/><path d="M554 58 L536 70 L554 82Z" fill="#ee8a1f"/>
    <path d="M310 110 H178" stroke="#1d5ea8" stroke-width="8"/><path d="M178 98 L160 110 L178 122Z" fill="#1d5ea8"/>
    <path d="M544 110 H676" stroke="#1d5ea8" stroke-width="8"/><path d="M676 98 L694 110 L676 122Z" fill="#1d5ea8"/>
    <path d="M427 104 V130 M360 130 H494 M360 130 V150 M427 130 V150 M494 130 V150" stroke="#1d5ea8" stroke-width="3" fill="none"/>
  </svg>
  <div class="flow-center">
    <span class="tag">ストレスフリー</span>
    <div class="node">健康診断<br>Web問診<br>サービス</div>
    <div class="cap">ワークフロー</div>
  </div>
  <div class="flow-label left">ご利用者がインターネットで問診表を入力</div>
  <div class="flow-label right">医療従事者が問診表、返答します。</div>
</section>

<h2 class="section-head benefits-head">■Web問診サービス<span class="num">4</span>つの利点<span class="rule"></span></h2>

<section class="cards benefits">
  <article class="card">
    <div class="card-top"><div class="badge c-red">1</div><div class="card-title">問診表の<br>データ化</div></div>
    <div class="kicker">Good Point</div>
    <p>問診をデータ化することで、紙の使用量を削減。保管や検索も簡単です。</p>
    <div class="pic" role="img" aria-label="書類とパソコンのアイコン"></div>
  </article>
  <article class="card">
    <div class="card-top"><div class="badge c-orange">2</div><div class="card-title">クイック<br>回答</div></div>
    <div class="kicker">Good Point</div>
    <p>スマホ・タブレットからご都合の良いタイミングで回答できます。</p>
    <div class="pic" role="img" aria-label="Q&Aのアイコン"></div>
  </article>
  <article class="card">
    <div class="card-top"><div class="badge c-green">3</div><div class="card-title">簡単出力</div></div>
    <div class="kicker">Good Point</div>
    <p>集計結果をCSV出力できます。</p>
    <div class="pic" role="img" aria-label="プリンターのアイコン"></div>
  </article>
  <article class="card">
    <div class="card-top"><div class="badge c-sky">4</div><div class="card-title">質問を<br>カスタマイズ</div></div>
    <div class="kicker">Good Point</div>
    <p>質問事項は必要に応じてオリジナルでカスタマイズが可能です。</p>
    <div class="pic" role="img" aria-label="握手のアイコン"></div>
  </article>
</section>

<h2 class="section-head steps-head">サービスご利用までの流れ</h2>

<section class="cards steps">
  <article class="card">
    <div class="card-top"><div class="badge c-red">1</div><div class="card-title">ご要望送付</div></div>
    <div class="kicker">STEP</div>
    <p>まずはご連絡ください。担当よりご要望を伺い、内容をご確認いたします。</p>
    <div class="pic" role="img" aria-label="メールのアイコン"></div>
  </article>
  <article class="card">
    <div class="card-top"><div class="badge c-orange">2</div><div class="card-title">解決策ご提案</div></div>
    <div class="kicker">STEP</div>
    <p>お客様の課題に最適なシステムの構成と導入方法をご提案します。</p>
    <div class="pic" role="img" aria-label="打ち合わせのアイコン"></div>
  </article>
  <article class="card">
    <div class="card-top"><div class="badge c-gray">3</div><div class="card-title">見積提出</div></div>
    <div class="kicker">STEP</div>
    <p>お見積りをご提出します。</p>
    <div class="pic" role="img" aria-label="見積書のアイコン"></div>
  </article>
  <article class="card">
    <div class="card-top"><div class="badge c-orange">4</div><div class="card-title">導入ご案内</div></div>
    <div class="kicker">STEP</div>
    <p>導入スケジュールをご案内し、運用開始までサポートします。</p>
    <div class="pic" role="img" aria-label="握手のアイコン"></div>
  </article>
</section>

<footer class="footer">
  <div class="company">株式会社ミライヘルスリンク</div>
  <div class="address">〒000-0000 架空県みどり市中央1-2-3 サンプルビル2F</div>
  <div class="note">お気軽にお問い合わせください</div>
  <div class="tel"><div><span>TEL</span>000-123-4501</div><div><span>FAX</span>000-123-4502</div></div>
</footer>

</body>
</html>
```